Lumo Nutrition Boost

We need a label designed for 4 different Vitamins. Dr. Lumo is a Chiropractor and would like to add few vitamins that help his patients and other people in need. Our logo is black and white which I will share below. We want something that stands out, attracts all age clients, and is easy to read and remember. Needs to be catchy just like the Brand Name - "Lumo" The Logo will be switched. Instead of it saying Spinal & Motion Care, it should say Nutrition on top and Boost on the bottom. Below is also my idea roughly on the designs, but open to your ideas and the name is what we want to go with. Also providing couple designs that were worked on under a different account by one of our collaborators. Thank You, Tova

```html
<!DOCTYPE html>
<html lang="en">
<head>
<meta charset="UTF-8">
<title>Lumo – Vital Shield Multivitamin Label</title>
<link rel="stylesheet" href="https://fonts.googleapis.com/css2?family=Fredoka:wght@600&family=Roboto+Slab:wght@800&family=Montserrat:wght@700;800&display=swap">
<style>
  :root {
    --backdrop: #ececec;
    --label: #ffffff;
    --citrus: #f9b42d;
    --citrus-soft: #fcd27a;
    --ink: #3b3b3b;
    --ink-deep: #2f2f2f;
    --faint: #f4f4f4;
  }
  * { margin: 0; padding: 0; box-sizing: border-box; }
  html, body {
    width: 1200px;
    height: 1200px;
    overflow: hidden;
    background: var(--backdrop);
  }
  .canvas {
    position: relative;
    width: 1200px;
    height: 1200px;
  }
  .label {
    position: absolute;
    left: 310px;
    top: 355px;
    width: 610px;
    height: 748px;
    background: var(--label);
  }
  .band {
    position: absolute;
    left: 0;
    width: 100%;
    height: 32px;
    background: var(--citrus);
  }
  .band--top { top: 5px; }
  .band--bottom { bottom: 5px; }

  .citrus-pattern {
    position: absolute;
    border-radius: 50%;
    background: var(--faint);
  }
  .citrus-pattern--a { left: 40px; top: 85px; width: 100px; height: 130px; }
  .citrus-pattern--b { left: 95px; top: 215px; width: 110px; height: 120px; }
  .citrus-pattern--c { left: 435px; top: 215px; width: 110px; height: 120px; }
  .citrus-pattern--d { left: 510px; top: 50px; width: 90px; height: 120px; }
  .citrus-pattern--e { left: 40px; top: 535px; width: 105px; height: 120px; }

  .brand {
    position: absolute;
    left: 0;
    top: 125px;
    width: 100%;
    display: flex;
    align-items: center;
    justify-content: center;
    gap: 16px;
  }
  .brand__dot {
    width: 34px;
    height: 34px;
    border-radius: 50%;
    background: var(--ink-deep);
  }
  .brand__name {
    font-family: "Montserrat", sans-serif;
    font-weight: 800;
    font-size: 78px;
    color: var(--ink-deep);
    line-height: 1;
  }

  .product-name {
    position: absolute;
    left: 0;
    top: 372px;
    width: 100%;
    text-align: center;
    font-family: "Fredoka", sans-serif;
    font-weight: 600;
    font-size: 62px;
    letter-spacing: 1px;
    color: var(--citrus);
    white-space: nowrap;
    line-height: 1;
  }

  .category {
    position: absolute;
    left: 85px;
    top: 465px;
    width: 425px;
    height: 60px;
    background: var(--ink);
    display: flex;
    align-items: center;
    justify-content: center;
    font-family: "Roboto Slab", serif;
    font-weight: 800;
    font-size: 27px;
    letter-spacing: 2px;
    color: var(--citrus);
  }

  .citrus-icon {
    position: absolute;
    left: 485px;
    top: 550px;
    width: 82px;
    height: 82px;
    border-radius: 50%;
    background: var(--citrus-soft);
  }

  .count {
    position: absolute;
    left: 0;
    top: 653px;
    width: 100%;
    text-align: center;
    font-family: "Montserrat", sans-serif;
    color: var(--ink-deep);
    line-height: 1;
  }
  .count__qty {
    display: block;
    font-weight: 800;
    font-size: 30px;
    letter-spacing: 1px;
  }
  .count__type {
    display: block;
    margin-top: 6px;
    font-weight: 700;
    font-size: 13px;
    letter-spacing: 2px;
  }
</style>
</head>
<body>
<main class="canvas">
  <section class="label">
    <div class="band band--top"></div>

    <div class="citrus-pattern citrus-pattern--a" role="img" aria-label="Faint citrus slice pattern"></div>
    <div class="citrus-pattern citrus-pattern--b" role="img" aria-label="Faint citrus slice pattern"></div>
    <div class="citrus-pattern citrus-pattern--c" role="img" aria-label="Faint citrus slice pattern"></div>
    <div class="citrus-pattern citrus-pattern--d" role="img" aria-label="Faint citrus slice pattern"></div>
    <div class="citrus-pattern citrus-pattern--e" role="img" aria-label="Faint citrus slice pattern"></div>

    <div class="brand">
      <span class="brand__dot"></span>
      <span class="brand__name">Lumo</span>
    </div>

    <h1 class="product-name">VITAL SHIELD</h1>

    <div class="category">MULTIVITAMIN</div>

    <div class="citrus-icon" role="img" aria-label="Citrus slice illustration"></div>

    <p class="count">
      <span class="count__qty">60 CAPSULES</span>
      <span class="count__type">DIETARY SUPPLEMENT</span>
    </p>

    <div class="band band--bottom"></div>
  </section>
</main>
</body>
</html>
```